【 概要 】 弊社の採用募集用のバナー制作をお願いいたします。 大々的に広告を打つので、複数で採用で検討しております。 また、弊社には現在、似たような案件が多いため、『キーワードだけ変えていただき採用』なども検討しており、目安は10名近い採用を考えておりますので奮ってご応募くださいませ。 年内で急ぎたいため、早期終了も検討しておりますのでお早めにどうぞ! 【 依頼内容 】 ・サイズ: 横1200 × 縦1200px ・作成数: 2種類(採用確定した方だけ、全く同じデザインで縦長へ配置換えをしたリサイズもお願いいたします) ・利用用途:リスティング広告、ウェブサイトなど ・キーワード:テキストファイルに添付 ・納品:ご提案はPNG。自社で微調整のために、採用された方のみ編集できるようPSDデータも納品お願いいたします。 【 デザインイメージ 】 ・ターゲット層:20〜40代の女性 ・雰囲気:構成などは全てお任せ 【 契約金額(税抜) 】 15000円 ※契約金額(税込)からシステム利用料を差し引いた金額が、ワーカーさまの受取金額となります その他ご質問等ありましたら、気軽にお問い合わせください。 ご応募をお待ちしております! |
とてもカラフルでインパクトが強い作品で理想と感じました。
たくさんのご応募ありがとうございました。
まずは1位採用で確定させていただきましたが、今回は複数採用でぜひ他にも気になる素敵な作品がございますので、別途またご連絡させていただきます方はご対応よろしくお願いいたします。

```html
<!DOCTYPE html>
<html lang="ja">
<head>
<meta charset="UTF-8">
<title>アプリモニター募集バナー</title>
<link href="https://fonts.googleapis.com/css2?family=Noto+Sans+JP:wght@500;700;900&display=swap" rel="stylesheet">
<style>
  :root {
    --frame: #ec5a6c;
    --bg-light: #fcc7b8;
    --bg-mid: #f8a295;
    --bg-pink: #f58a9e;
    --accent-orange: #f7892c;
    --band-start: #f5874a;
    --band-end: #eb3f5e;
    --white: #ffffff;
    --photo-top: #f4ddd6;
    --photo-bottom: #2c2f3a;
  }
  * { margin: 0; padding: 0; box-sizing: border-box; }
  html, body { width: 1200px; height: 1200px; overflow: hidden; background: #fff; }
  .banner {
    position: relative;
    width: 1200px;
    height: 1200px;
    overflow: hidden;
    background: var(--frame);
    font-family: "Noto Sans JP", sans-serif;
  }
  .banner-field {
    position: absolute;
    inset: 8px;
    background:
      linear-gradient(125deg, rgba(255,255,255,0.18) 0 38%, rgba(255,255,255,0) 38% 100%),
      linear-gradient(160deg, var(--bg-light) 0%, var(--bg-mid) 45%, var(--bg-pink) 100%);
    overflow: hidden;
  }
  .model-photo {
    position: absolute;
    left: 810px;
    top: 50px;
    width: 382px;
    height: 1142px;
    border-radius: 190px 0 0 0;
    background: linear-gradient(180deg, var(--photo-top) 0%, #ecc7bb 30%, #b88f8a 42%, var(--photo-bottom) 58%, #1f222b 100%);
  }
  .speech-bubble {
    position: absolute;
    left: 59px;
    top: 62px;
    width: 714px;
    height: 300px;
  }
  .speech-bubble svg { position: absolute; inset: 0; }
  .bubble-text {
    position: absolute;
    left: 0; top: 0;
    width: 714px;
    padding: 34px 44px 0 44px;
    color: var(--accent-orange);
    font-weight: 900;
    font-size: 84px;
    line-height: 1.2;
    white-space: nowrap;
  }
  .bubble-text span { display: block; }
  .bubble-text .line-2 { text-align: right; }
  .phone-icon {
    position: absolute;
    left: 160px;
    top: 262px;
    width: 190px;
    height: 220px;
  }
  .pay-rate {
    position: absolute;
    left: 90px;
    color: var(--white);
    font-weight: 900;
    text-shadow: 0 3px 8px rgba(200, 60, 70, 0.25);
    white-space: nowrap;
    line-height: 1;
  }
  .pay-rate.unit-time { top: 462px; }
  .pay-rate.amount { top: 722px; }
  .pay-rate .big { font-size: 160px; }
  .pay-rate .unit { font-size: 80px; }
  .pay-rate .huge { font-size: 168px; letter-spacing: -2px; }
  .tagline-band {
    position: absolute;
    left: 59px;
    top: 966px;
    width: 1082px;
    height: 126px;
    background: linear-gradient(90deg, var(--band-start), var(--band-end));
    display: flex;
    align-items: center;
    justify-content: center;
    color: var(--white);
    font-weight: 500;
    font-size: 82px;
    letter-spacing: 2px;
    white-space: nowrap;
    box-shadow: 0 6px 18px rgba(180, 40, 60, 0.25);
  }
</style>
</head>
<body>
  <div class="banner">
    <div class="banner-field"></div>

    <div class="model-photo" role="img" aria-label="スーツ姿で笑顔の女性スタッフが手のひらで案内している写真"></div>

    <div class="speech-bubble">
      <svg viewBox="0 0 714 300" width="714" height="300" aria-hidden="true">
        <path d="M40 0 H674 Q714 0 714 40 V240 Q714 276 678 276 H230 L150 300 L165 276 H40 Q0 276 0 236 V40 Q0 0 40 0 Z" fill="#ffffff"/>
      </svg>
      <div class="bubble-text">
        <span class="line-1">アプリモニター</span>
        <span class="line-2">募集!</span>
      </div>
    </div>

    <svg class="phone-icon" viewBox="0 0 190 220" aria-hidden="true">
      <g transform="rotate(-14 95 110)">
        <rect x="40" y="15" width="112" height="190" rx="18" fill="var(--accent-orange)"/>
        <rect x="53" y="34" width="86" height="130" rx="4" fill="#ffffff"/>
        <circle cx="96" cy="184" r="9" fill="#ffffff"/>
      </g>
    </svg>

    <div class="pay-rate unit-time"><span class="big">1</span><span class="unit">時間</span></div>
    <div class="pay-rate amount"><span class="huge">2,500</span><span class="unit">円~</span></div>

    <div class="tagline-band">自宅でカンタンお仕事!</div>
  </div>
</body>
</html>
```